Diabetes Education Flyer Design Project

We need a 8.5" X 11" flyer design for a retail pharmacy located in Queens, NYC to promote our new program of "Free Diabetes Education". This flyer will be distributed to doctors offices and to places where people congregate. The flyer should create a fear to the audience about diabetes and an urgency to come or call the pharmacy to get more information on the "Free Diabetes Education". The target audience is 40+ years old with national background of West Indies and India. They are mostly blue color worker with a highschool or less education

Target Market(s)

People with diabetes aging 40+, from West Indies and India, low literacy level

Industry/Entity Type

Education

Requirements
Must have
• Must have graphics and colors to attract the targetted age/race/literacy. Must have graphics and colors to create fear at the begining and hope at the end.
Nice to have
• Fonts to support the theme

```html
<!DOCTYPE html>
<html lang="en">
<head>
<meta charset="utf-8">
<title>Diabetes Education Flyer</title>
<link rel="stylesheet" href="https://fonts.googleapis.com/css2?family=Alegreya+Sans+SC:wght@800&family=Open+Sans:wght@400;600;700&display=swap">
<style>
  :root {
    --page-bg: #eef0f1;
    --stone-light: #d9dad6;
    --stone-mid: #b9bbb6;
    --panel-dark: #5f605e;
    --panel-mid: #8a8b88;
    --ink: #1b1b1b;
    --offer-box: #dfe7ea;
    --teal: #3bb3c3;
    --brand: #e3245b;
    --xray-dark: #1f2426;
    --xray-bone: #7f8a8d;
  }
  * { margin: 0; padding: 0; box-sizing: border-box; }
  html, body { width: 1200px; height: 910px; overflow: hidden; background: var(--page-bg); }
  body { position: relative; font-family: "Open Sans", Arial, sans-serif; color: var(--ink); }

  .flyer {
    position: absolute; left: 284px; top: 35px; width: 635px; height: 840px;
    background: radial-gradient(ellipse at 30% 20%, var(--stone-light), var(--stone-mid) 70%, #a9aba6);
    box-shadow: 0 0 6px rgba(0,0,0,.15);
  }
  .warning-panel {
    position: absolute; left: 29px; top: 23px; width: 581px; height: 560px;
    border-radius: 32px 32px 0 0;
    background: linear-gradient(to bottom, var(--panel-dark) 0%, #6c6d6a 55%, var(--panel-mid) 85%, #9a9b98 100%);
  }
  .headline {
    position: absolute; left: 0; width: 100%; text-align: center;
    font-family: "Alegreya Sans SC", "Arial Black", sans-serif; font-weight: 800;
    line-height: 1; color: var(--ink);
  }
  .headline--fact { top: 44px; font-size: 33px; line-height: 39px; }
  .headline--question { top: 166px; font-size: 46px; }

  .xray {
    position: absolute; left: 148px; top: 226px; width: 269px; height: 265px;
    border: 4px solid #2c2f30; border-radius: 4px;
    background: radial-gradient(ellipse 35% 55% at 45% 50%, var(--xray-bone), #3a4143 70%, var(--xray-dark));
  }
  .xray-caption {
    position: absolute; top: 494px; width: 100%; text-align: center;
    font-size: 14px; font-weight: 400; line-height: 18px; color: var(--ink);
  }

  .offer-box {
    position: absolute; left: 29px; top: 545px; width: 581px; height: 152px;
    background: var(--offer-box); border-radius: 4px;
    text-align: center; color: var(--teal);
  }
  .brand { display: inline-flex; align-items: center; gap: 8px; margin-top: 14px;
    font-size: 26px; font-weight: 700; color: var(--brand); line-height: 1; }
  .brand-dot { width: 12px; height: 12px; background: var(--brand); }
  .offer-intro { font-size: 13px; margin-top: 6px; }
  .offer-title { font-size: 22px; font-weight: 600; line-height: 1.1; }
  .offer-call { font-size: 13px; font-weight: 600; margin-top: 4px; }
  .offer-tagline { font-size: 13px; font-weight: 600; }

  .contact {
    position: absolute; top: 713px; width: 100%; text-align: center;
    font-size: 14px; line-height: 19px; font-style: normal;
  }
  .source {
    position: absolute; left: 17px; top: 768px; width: 601px;
    border-top: 1px solid var(--ink); padding-top: 8px;
    text-align: center; font-size: 7.6px; line-height: 11px; font-weight: 600;
    white-space: nowrap;
  }
</style>
</head>
<body>
  <article class="flyer">
    <section class="warning-panel">
      <h1 class="headline headline--fact">Diabetes<br>Kills 3,400,000 People<br>In a Year</h1>
      <h2 class="headline headline--question">Are You the Next?</h2>
      <div class="xray" role="img" aria-label="Digital X-ray of a diabetic person's foot"></div>
      <p class="xray-caption">Digital foot xray of a person with diabetes</p>
    </section>

    <section class="offer-box">
      <div class="brand"><span class="brand-dot"></span>Northgate Pharmacy</div>
      <p class="offer-intro">is offering</p>
      <p class="offer-title">FREE Education for Diabetics</p>
      <p class="offer-call">Call or Stop by Now! Your Life Depends on It!</p>
      <p class="offer-tagline">Educate yourself and Live Longer</p>
    </section>

    <address class="contact">
      Northgate Pharmacy<br>
      84-20 Maple Ave., Kew Gardens, NY 11415<br>
      (718) 555-0142
    </address>

    <p class="source">
      According to International Health Bureau in 2004, an estimated 3.4 million people died worldwide from consequences of high blood sugar.<br>
      Fact Sheet No. 312 (August,2011)
    </p>
  </article>
</body>
</html>
```